Pellam Brochure

Morvik & Dunsley Education Group was formed in 2011 as an organizational arm
to put educational and charitable services together for community
development.

M & D was acquired by Pellam Education Group in 2013 and relocated to Texas
with the expressed focus of reaching underserved communities and
population, both in the Dallas- Fort Worth Metropolitan area and Houston
areas. Key members of the organization are based in Dallas, TX, Houston,
TX, Atlanta GA, and Washington DC and are strategically networked to
utilize their external resources for education advancement with
under-served populations.

Target Market(s)

- -The target market is 17-45 year olds, the demographics are 70%
women, 30% men, interested in an entry level education in
the health field

Industry/Entity Type

Education

```html
<!DOCTYPE html>
<html lang="en">
<head>
<meta charset="utf-8">
<title>Pellam Brochure</title>
<link href="https://fonts.googleapis.com/css2?family=Crimson+Text:ital,wght@0,700;1,700&family=Didact+Gothic&family=Oswald:wght@600&family=Arimo:wght@700&display=swap" rel="stylesheet">
<style>
  :root {
    --green: #8dc63f;
    --green-light: #a9d24a;
    --blue: #115b8f;
    --blue-deep: #0b4d7c;
    --ink: #3a3a3a;
    --paper: #ffffff;
  }
  * { box-sizing: border-box; margin: 0; padding: 0; }
  html, body { width: 1200px; height: 465px; overflow: hidden; background: var(--paper); }
  .brochure { position: relative; width: 1200px; height: 465px; overflow: hidden; font-family: "Didact Gothic", sans-serif; }

  /* Application panel */
  .application { position: absolute; left: 0; top: 0; width: 300px; height: 453px; background: var(--paper); }
  .application-title { position: absolute; top: 30px; left: 0; width: 320px; text-align: center; font-family: "Crimson Text", serif; font-style: italic; font-weight: 700; font-size: 14px; color: var(--green); }
  .form { position: absolute; top: 68px; left: 20px; width: 274px; font-size: 6.6px; color: var(--ink); }
  .field { display: flex; align-items: flex-end; height: 10.3px; white-space: nowrap; }
  .field .line { flex: 1; border-bottom: 0.6px solid #555; margin-left: 1px; height: 7px; }
  .field .short { flex: 0 0 52px; }
  .gap { height: 10px; }

  /* Mission panel */
  .mission-panel { position: absolute; left: 300px; top: 0; width: 301px; height: 453px; background: var(--blue); color: #e6eef5; }
  .mission-photo { position: absolute; left: 0; top: 0; width: 301px; height: 217px; background: linear-gradient(160deg, #eef0ee 0%, #d9dcd6 40%, #7fbf4a 60%, #c9cfd0 100%); }
  .panel-heading { font-family: "Crimson Text", serif; font-style: italic; font-weight: 700; color: var(--green-light); font-size: 13px; text-align: center; }
  .mission-heading { position: absolute; top: 240px; left: 0; width: 301px; }
  .mission-text { position: absolute; top: 268px; left: 24px; width: 262px; font-size: 6.4px; line-height: 10px; }
  .history-heading { position: absolute; top: 309px; left: 0; width: 301px; }
  .history-text { position: absolute; top: 334px; left: 24px; width: 262px; font-size: 6.4px; line-height: 10px; }
  .history-text p + p { margin-top: 9px; }

  /* Cover panel */
  .cover { position: absolute; left: 601px; top: 0; width: 599px; height: 453px; }
  .cover svg { position: absolute; left: 0; top: 0; }
  .brand { position: absolute; top: 82px; right: 32px; display: flex; align-items: center; gap: 4px; font-size: 9.5px; color: var(--blue); white-space: nowrap; }
  .brand-dot { width: 9px; height: 9px; border-radius: 50%; background: var(--green); }
  .tagline { position: absolute; top: 220px; left: 457px; width: 142px; height: 66px; background: var(--green); color: #fff; font-family: "Oswald", sans-serif; font-weight: 600; text-align: center; line-height: 1.15; padding-top: 4px; }
  .tagline .t1 { font-size: 20px; }
  .tagline .t2 { font-size: 10.5px; }
  .tagline .t3 { font-size: 16px; }
  .service-heading { position: absolute; top: 228px; left: 42px; font-family: "Crimson Text", serif; font-weight: 700; font-size: 13px; color: var(--green); }
  .service-text { position: absolute; top: 258px; left: 26px; width: 254px; font-size: 7.3px; line-height: 10.8px; color: #222; }
  .service-text p + p { margin-top: 10.8px; }
  .contact { position: absolute; top: 416px; left: 80px; width: 120px; text-align: center; font-family: "Arimo", sans-serif; font-weight: 700; font-size: 9.5px; line-height: 12.5px; color: var(--green-light); }
  .cover-web { position: absolute; top: 431px; left: 450px; font-size: 10.5px; color: var(--green-light); white-space: nowrap; }

  .base-band { position: absolute; left: 0; top: 453px; width: 1200px; height: 12px; background: var(--green); }
</style>
</head>
<body>
<div class="brochure">

  <section class="application">
    <h2 class="application-title">Application for Admission</h2>
    <div class="form">
      <div class="field">Full Name:<span class="line"></span></div>
      <div class="field">Last<span class="line"></span></div>
      <div class="field">First<span class="line"></span></div>
      <div class="field">Middle<span class="line"></span></div>
      <div class="field">DOB:<span class="line"></span></div>
      <div class="field">Address:<span class="line"></span></div>
      <div class="field">Street Address<span class="line"></span></div>
      <div class="field">Apartment/Unit #<span class="line"></span></div>
      <div class="gap"></div>
      <div class="field">City<span class="line short"></span>State<span class="line short"></span>ZIP Code<span class="line"></span></div>
      <div class="field">Phone:<span class="line"></span></div>
      <div class="field">Email<span class="line"></span></div>
      <div class="field">Social Security<span class="line"></span></div>
      <div class="field">High School/ GED:<span class="line"></span></div>
      <div class="field">Graduation Year:<span class="line"></span></div>
      <div class="field">Semester: &nbsp;&nbsp;(Winter) &nbsp;&nbsp;&nbsp;(Spring) &nbsp;&nbsp;&nbsp;(Summer) &nbsp;&nbsp;&nbsp;(Fall)</div>
      <div class="field">Are you a citizen of the United States? &nbsp;YES OR &nbsp;&nbsp;NO</div>
      <div class="field">If no, are you authorized to work in the U.S.? &nbsp;&nbsp;&nbsp;YES</div>
      <div class="field">OR &nbsp;&nbsp;&nbsp;NO</div>
      <div class="field">Have you ever been convicted of a felony? &nbsp;&nbsp;&nbsp;YES</div>
      <div class="field">OR &nbsp;&nbsp;&nbsp;NO</div>
      <div class="field">If yes, explain:<span class="line"></span></div>
      <div class="field"><span class="line"></span></div>
      <div class="field"><span class="line"></span></div>
      <div class="field"><span class="line"></span></div>
      <div class="field">Education<span class="line"></span></div>
      <div class="field">High School<span class="line"></span></div>
      <div class="field">Address:<span class="line"></span></div>
      <div class="field"><span class="line"></span></div>
      <div class="field"><span class="line"></span></div>
      <div class="field">From:<span class="line short"></span>&nbsp;To:<span class="line"></span></div>
      <div class="field">Did you graduate? &nbsp;&nbsp;&nbsp;YES OR &nbsp;&nbsp;NO</div>
      <div class="field">OR</div>
      <div class="field">Diploma:</div>
    </div>
  </section>

  <section class="mission-panel">
    <div class="mission-photo" role="img" aria-label="Photo of a smiling student holding a red folder, with classmates behind her"></div>
    <h3 class="panel-heading mission-heading">Our Mission</h3>
    <p class="mission-text">"Our primary mission is to develop high quality health professionals with the inspiration positively effect their families, communities and professions."</p>
    <h3 class="panel-heading history-heading">History</h3>
    <div class="history-text">
      <p>Morvik &amp; Dunsley Education Group was formed in 2011 as an organizational arm to put educational and charitable services together for community development.</p>
      <p>M &amp; D was acquired by Pellam Education Group in 2013 and relocated to Texas with the expressed focus of reaching underserved communities and population, both in the Dallas- Fort Worth Metropolitan area and Houston areas. Key members of the organization are based in Dallas, TX, Houston, TX and Washington DC and are strategically networked to utilize their external resources for education advancement with under-served populations.</p>
    </div>
  </section>

  <section class="cover">
    <svg width="599" height="453" viewBox="0 0 599 453">
      <defs>
        <linearGradient id="crowd" x1="0" y1="0" x2="1" y2="1">
          <stop offset="0" stop-color="#f4f4f2"/>
          <stop offset="0.45" stop-color="#d8cfc4"/>
          <stop offset="0.75" stop-color="#b9a58e"/>
          <stop offset="1" stop-color="#e8e6e2"/>
        </linearGradient>
      </defs>
      <rect class="cover-base" width="599" height="453" fill="#115b8f"/>
      <rect class="cover-photo" width="599" height="330" fill="url(#crowd)" role="img" aria-label="Photo of a cheerful group of adults jumping with arms raised"/>
      <path class="cover-sweep" d="M0,212 C90,190 180,188 260,196 C380,208 500,230 599,250 L599,415 C440,410 280,392 0,380 Z" fill="#ffffff"/>
      <path d="M0,212 C90,190 180,188 260,196" fill="none" stroke="#115b8f" stroke-width="5"/>
      <path d="M30,378 C250,392 430,410 599,413" fill="none" stroke="#8dc63f" stroke-width="6"/>
    </svg>
    <div class="brand"><span class="brand-dot"></span>Pellam Education Group</div>
    <div class="tagline">
      <div class="t1">Connecting</div>
      <div class="t2">Your Training To</div>
      <div class="t3">Your Purpose...</div>
    </div>
    <h3 class="service-heading">Home Health Aide</h3>
    <div class="service-text">
      <p>As home health care becomes more and more prominent, there is a growing need for Certified Home Health Aid Certified Home Health Aides are a very important piece of the Health Care Industry. Caring for a patient in their home can be difficult and challenging, but at the same time can be fun and rewarding. A successful HHA needs to possess unique skills that many other health care providers may not.</p>
      <p>At Pellam Education Group we currently offer a Home Health Aide Certification Program that develops the skills necessary for success in the health care industry.</p>
    </div>
    <div class="contact">www.PellamEd.com<br>512.555.0148</div>
    <div class="cover-web">www.PellamEd.com</div>
  </section>

  <div class="base-band"></div>
</div>
</body>
</html>
```